The most modern business card ever !!!

Our company call “Vantilo”. Vantilo is a technology company specialized in cruises solutions. Out main product is a platform to reserve cruises. This is a revolutionary platform that make easier to travel agencies and final users to reserve cruises across dozen companies like tarvik, welbi, dpv, hbt, etc..We are a “start up”, with a young team of developers and we want to transmit it.. For it, we want something different, a modern business card that represent cruises and technology.. When someone receive this card, this person should say: wowww this is different… this is modern… this is a cruise related company..
Contact Information for Business Card
Requirements
Must have
- diferent, modern
Should not have
- traditions business card

```html
<!DOCTYPE html>
<html lang="en">
<head>
<meta charset="utf-8">
<title>Vantilo Business Card</title>
<link href="https://fonts.googleapis.com/css2?family=Hind:wght@500;600&family=Arimo:wght@400&family=Montserrat:wght@300;400;700&display=swap" rel="stylesheet">
<style>
  :root {
    --teal: #217470;
    --sky: #33ade0;
    --ink: #1c2424;
    --tile: rgba(168, 204, 204, 0.2);
    --paper: #ffffff;
  }
  html, body {
    margin: 0;
    padding: 0;
    width: 1200px;
    height: 734px;
    overflow: hidden;
    background: var(--paper);
  }
  .card {
    position: relative;
    width: 1200px;
    height: 734px;
    box-sizing: border-box;
    border: 1px solid #333;
    background: var(--paper);
    overflow: hidden;
    font-family: "Hind", sans-serif;
    color: var(--ink);
  }
  .side-band {
    position: absolute;
    left: 0; top: 0;
    width: 130px; height: 734px;
    background: var(--teal);
  }
  .edge-bar {
    position: absolute;
    left: 1174px; top: 234px;
    width: 26px; height: 281px;
    background: var(--teal);
  }
  .tiles {
    position: absolute;
    left: 0; top: 0;
  }
  .icon-badge {
    position: absolute;
    width: 92px; height: 92px;
    border-radius: 50%;
    background: var(--sky);
    display: flex;
    align-items: center;
    justify-content: center;
  }
  .contact-title {
    position: absolute;
    margin: 0;
    font-weight: 600;
    font-size: 40px;
    line-height: 1;
    letter-spacing: 0.5px;
  }
  .contact-value {
    position: absolute;
    margin: 0;
    font-weight: 500;
    font-size: 25px;
    line-height: 1;
    letter-spacing: 0.6px;
  }
  .contact-value.plain {
    font-family: "Arimo", sans-serif;
    font-weight: 400;
    font-size: 23px;
    letter-spacing: 0.3px;
  }
  .vertical {
    position: absolute;
    transform-origin: center;
    transform: translate(-50%, -50%) rotate(-90deg);
    white-space: nowrap;
    font-family: "Montserrat", sans-serif;
    line-height: 1;
  }
  .person-name {
    left: 967px; top: 367px;
    font-size: 36px;
    font-weight: 300;
    letter-spacing: 1px;
  }
  .person-name strong { font-weight: 700; }
  .person-role {
    left: 1009px; top: 366px;
    font-size: 17px;
    font-weight: 400;
    letter-spacing: 1px;
  }
  .brand-name {
    left: 1131px; top: 378px;
    font-size: 52px;
    font-weight: 700;
    letter-spacing: 1px;
    color: var(--ink);
  }
</style>
</head>
<body>
<div class="card">
  <svg class="tiles" width="1200" height="734" viewBox="0 0 1200 734" aria-hidden="true">
    <rect x="840" y="53" width="224" height="216" rx="50" fill="rgba(168,204,204,0.08)"/>
    <rect x="42" y="114" width="312" height="318" rx="60" fill="var(--tile)"/>
    <rect x="234" y="72" width="441" height="442" rx="80" fill="var(--tile)"/>
    <rect x="140" y="222" width="335" height="337" rx="60" fill="var(--tile)"/>
    <rect x="568" y="192" width="229" height="228" rx="50" fill="var(--tile)"/>
    <rect x="682" y="128" width="229" height="229" rx="50" fill="var(--tile)"/>
    <rect x="706" y="253" width="441" height="408" rx="70" fill="var(--tile)"/>
    <rect x="593" y="466" width="335" height="268" rx="60" fill="var(--tile)"/>
    <rect x="297" y="445" width="331" height="289" rx="60" fill="rgba(168,204,204,0.12)"/>
  </svg>

  <div class="side-band"></div>
  <svg class="tiles" width="1200" height="734" viewBox="0 0 1200 734" aria-hidden="true">
    <rect x="42" y="114" width="312" height="318" rx="60" fill="rgba(255,255,255,0.06)"/>
    <rect x="140" y="222" width="335" height="337" rx="60" fill="rgba(255,255,255,0.05)"/>
  </svg>
  <div class="edge-bar"></div>

  <div class="icon-badge" style="left:83px; top:168px;">
    <svg width="40" height="40" viewBox="0 0 24 24" aria-hidden="true">
      <path d="M6.6 2.5c.6-.3 1.2 0 1.5.5l2 3.8c.3.5.1 1.1-.3 1.4l-1.6 1.1c.7 2.3 2 4.6 3.8 6.5l1.6-1c.5-.3 1.1-.2 1.4.3l2.4 3.5c.3.5.2 1.2-.3 1.5l-1.6 1.1c-.9.6-2.1.6-3-.1C8.4 18.3 5.3 13 4.6 7.6c-.2-1.1.3-2.1 1.2-2.7z" fill="var(--ink)"/>
    </svg>
  </div>
  <h2 class="contact-title" style="left:221px; top:180px;">Your Phone</h2>
  <p class="contact-value" style="left:221px; top:227px;">+612-734-5190</p>

  <div class="icon-badge" style="left:83px; top:321px;">
    <svg width="40" height="30" viewBox="0 0 40 30" aria-hidden="true">
      <rect x="2" y="3" width="36" height="24" rx="2" fill="none" stroke="#2a3a44" stroke-width="3"/>
      <path d="M3 5 L20 17 L37 5" fill="none" stroke="#2a3a44" stroke-width="3"/>
    </svg>
  </div>
  <h2 class="contact-title" style="left:221px; top:333px;">Your E-mail</h2>
  <p class="contact-value" style="left:219px; top:386px;">nadiru@vantilo.com</p>

  <div class="icon-badge" style="left:83px; top:474px;">
    <svg width="30" height="34" viewBox="0 0 30 34" aria-hidden="true">
      <rect x="2" y="2" width="26" height="30" fill="none" stroke="var(--ink)" stroke-width="3"/>
      <rect x="7" y="8" width="7" height="7" fill="var(--ink)"/>
      <rect x="7" y="18" width="7" height="7" fill="var(--ink)"/>
      <rect x="16" y="18" width="7" height="7" fill="var(--ink)"/>
    </svg>
  </div>
  <h2 class="contact-title" style="left:210px; top:486px;">Your Adress</h2>
  <p class="contact-value plain" style="left:210px; top:531px;">Marvelle, Sundara</p>

  <div class="icon-badge" style="left:831px; top:321px;">
    <svg width="44" height="40" viewBox="0 0 44 40" aria-hidden="true">
      <circle cx="12" cy="20" r="9" fill="var(--ink)"/>
      <path d="M20 20 L40 8 L40 32 Z" fill="var(--ink)"/>
    </svg>
  </div>

  <div class="vertical person-name"><strong>YOUR</strong> NAME</div>
  <div class="vertical person-role">YOUR POSITION</div>
  <div class="vertical brand-name">Vantilo</div>
</div>
</body>
</html>
```